Waterjet Cutting Business requires an up to date website

We currently have a website which is outdated and in need of modernization.
We are only looking for a simple website with around 4 pages: Home, Contact Us, Materials, Gallery.
We have some pictures and a logo which can be used.
Our primary business is profile cutting of materials to customers specifications using high-pressure water with abrasive.
We are looking for creative ideas and are open to suggestions!
http://brightfordcutworks.com/index.asp?pid=1
Update:
Cut quality picture (uploaded)
Map
Comparison to other profile cutting methods such as plasma/laser
Single page style without continuous scrolling
"We can cut virtually any material from any drawing whether it be a Full 3D cad models to hand sketched "
Target Market(s)
Film Industry, Prototype, Engineering, Architect, Artisits, one off designs
Industry/Entity Type
Engineering
Number of Pages Required
1 page
Font styles to use
Look and feel

```html
<!DOCTYPE html>
<html lang="en">
<head>
<meta charset="utf-8">
<title>Brightford Cutworks – Waterjet Profile Cutting</title>
<link rel="stylesheet" href="https://fonts.googleapis.com/css2?family=Exo+2:wght@400;500;600;700&family=Arimo:wght@400;700&display=swap">
<style>
:root{
  --blue:#1d6390;
  --blue-dark:#134a6e;
  --ink:#333a40;
  --muted:#5c6368;
  --light:#f1f4f6;
  --white:#ffffff;
  --hero-a:#3b3833;
  --hero-b:#6f6a62;
  --contact-a:#2f2f25;
  --contact-b:#4a4a3a;
  --steel-a:#8d8d8b;
  --steel-b:#c4c4c2;
}
*{box-sizing:border-box;margin:0;padding:0}
html,body{width:1200px;height:3495px;overflow:hidden}
body{position:relative;font-family:"Arimo",Arial,sans-serif;color:var(--ink);background:var(--white)}
.section{position:absolute;left:0;width:1200px;overflow:hidden}
.heading{font-family:"Exo 2",Arial,sans-serif;font-weight:600;color:var(--blue-dark);font-size:36px;position:absolute;left:142px}
.heading-mark{position:absolute;left:142px;width:16px;height:16px;background:var(--blue)}
.body-text{position:absolute;left:142px;width:918px;font-size:11px;line-height:19px;color:var(--muted)}
.side-label{position:absolute;width:60px;height:180px}
.side-label span{position:absolute;left:50%;top:50%;transform:translate(-50%,-50%) rotate(-90deg);font-family:"Exo 2",sans-serif;font-size:12px;color:var(--blue-dark);white-space:nowrap}
.side-label::before,.side-label::after{content:"";position:absolute;left:50%;width:1px;height:45px;background:var(--blue)}
.side-label::before{top:0}.side-label::after{bottom:0}
.side-label.on-dark span{color:var(--white)}
.side-label.on-dark::before,.side-label.on-dark::after{background:var(--white)}

/* hero */
.hero{top:0;height:635px;background:linear-gradient(170deg,var(--hero-b) 0%,var(--hero-a) 55%,#25231f 100%)}
.brand{position:absolute;left:0;width:1200px;top:125px;text-align:center;font-family:"Exo 2",sans-serif;font-weight:700;font-size:42px;letter-spacing:2px;color:var(--blue)}
.brand i{display:inline-block;width:22px;height:22px;background:var(--blue);margin-right:12px;vertical-align:middle}
.nav{position:absolute;top:258px;left:0;width:1200px;display:flex;justify-content:center;gap:30px}
.nav a{font-family:"Exo 2",sans-serif;font-weight:700;font-size:14px;color:var(--white);text-decoration:none;padding:6px 10px}
.nav a.active{background:var(--blue)}
.tagline{position:absolute;top:325px;left:0;width:1200px;text-align:center;font-family:"Exo 2",sans-serif;font-weight:600;font-size:27px;line-height:36px;color:var(--white)}
.btn{position:absolute;top:412px;left:519px;width:162px;height:38px;line-height:36px;text-align:center;background:var(--blue);border:1px solid #8fbcd8;color:var(--white);font-family:"Exo 2",sans-serif;font-weight:600;font-size:15px}

/* about */
.about{top:635px;height:340px;background:var(--white)}
/* quality */
.quality{top:975px;height:675px;background:var(--light)}
.cuts{position:absolute;left:154px;top:275px;display:flex;gap:5px}
.cut{width:174px}
.cut .sample{height:253px;background:linear-gradient(90deg,var(--steel-a),var(--steel-b),var(--steel-a))}
.cut h4{margin-top:18px;text-align:center;font-family:"Exo 2",sans-serif;font-weight:600;font-size:14px;color:var(--ink)}
.cut p{text-align:center;font-size:10px;line-height:12px;color:var(--ink);margin-top:4px}
/* materials */
.materials{top:1650px;height:455px;background:var(--white)}
.materials .body-text{width:505px}
.materials .body-text p{margin-bottom:8px}
.materials .lead{font-weight:700;color:var(--ink)}
.materials .cta{font-weight:700;color:var(--blue)}
.photo-frame{position:absolute;left:668px;top:150px;width:392px;height:240px;border:2px solid #ccc;padding:6px;background:var(--white)}
.photo-frame div{width:100%;height:100%;background:radial-gradient(circle at 60% 40%,#c98a3b,#3a2718 70%,#1a120c)}
/* gallery */
.gallery{top:2105px;height:730px;background:var(--light)}
.gallery .heading{font-weight:400;color:var(--ink)}
.grid{position:absolute;left:142px;top:185px;width:920px;display:grid;grid-template-columns:repeat(3,305px);grid-auto-rows:217px;gap:2px}
.tile{position:relative}
.tile.t1{background:linear-gradient(160deg,#3a3a3a,#7a3a1a 70%,#d0701e)}
.tile.t2{background:linear-gradient(150deg,#4d7fa6,#1f4f75);}
.tile.t3{background:radial-gradient(circle at 50% 60%,#2ec0c0,#0f1d22 65%)}
.tile.t4{background:linear-gradient(150deg,#15303f,#456a80)}
.tile.t5{background:radial-gradient(circle at 50% 50%,#4cd34c,#0c3d0c 75%)}
.tile.t6{background:radial-gradient(circle at 50% 60%,#e040d0,#2a0a30 75%)}
.tile .overlay{position:absolute;inset:0;background:rgba(29,99,144,.75);color:var(--white);text-align:center;padding:58px 22px 0}
.overlay h5{font-family:"Exo 2",sans-serif;font-size:18px;font-weight:600;margin-bottom:8px}
.overlay p{font-size:10px;line-height:13px}
.arrow{position:absolute;top:360px;width:30px;height:80px}
/* contact */
.contact{top:2835px;height:475px;background:radial-gradient(circle at 70% 30%,var(--contact-b),var(--contact-a) 70%)}
.contact .heading{color:var(--white);top:135px}
.info{position:absolute;left:142px;top:195px;color:var(--white);font-size:11px;line-height:15px}
.info .row{display:flex;gap:16px;margin-bottom:22px}
.info svg{flex:none}
.info b{display:block;margin-bottom:2px}
.form{position:absolute;left:652px;top:135px;width:408px}
.field{background:rgba(255,255,255,.92);height:32px;font-size:11px;padding:9px 10px;color:var(--ink);border-right:4px solid var(--white)}
.form .pair{display:flex;gap:12px;margin-top:9px}
.form .pair .field{flex:1}
.field.msg{height:118px;margin-top:9px}
.submit{margin-top:14px;width:162px;height:38px;background:var(--blue);border:1px solid #8fbcd8;color:var(--white);font-family:"Exo 2",sans-serif;font-weight:600;font-size:15px;display:flex;align-items:center;justify-content:center;gap:16px}
/* footer */
.footer{top:3310px;height:185px;background:var(--blue)}
.footer nav{position:absolute;top:26px;width:1200px;display:flex;justify-content:center;gap:44px}
.footer nav a{color:var(--white);font-family:"Exo 2",sans-serif;font-weight:700;font-size:14px;text-decoration:none}
.footer .brand{top:70px;font-size:32px;color:var(--white)}
.footer .brand i{background:var(--white);width:18px;height:18px}
.copyright{position:absolute;top:142px;width:1200px;text-align:center;color:var(--white);font-size:11px;font-weight:700}
</style>
</head>
<body>

<header class="section hero" role="img" aria-label="Photograph of a waterjet cutting head working over a cut metal plate">
  <div class="brand"><i></i>BRIGHTFORD CUTWORKS</div>
  <nav class="nav">
    <a class="active">Home</a><a>About Us</a><a>Method</a><a>Materials</a><a>Gallery</a><a>Contact Us</a>
  </nav>
  <h1 class="tagline">We can cut virtually any material from any drawing<br>whether it be a Full 3D cad models to hand sketched</h1>
  <a class="btn">Contact Us Today</a>
</header>

<section class="section about">
  <div class="side-label" style="left:42px;top:0"><span>About Us</span></div>
  <div class="heading-mark" style="top:100px"></div>
  <h2 class="heading" style="top:125px">About Brightford Cutworks</h2>
  <p class="body-text" style="top:180px">Lorem ipsum dolor sit amet, consectetuer adipiscing elit, sed diam nonummy nibh euismod tincidunt ut laoreet dolore magna aliquam erat volutpat. Ut wisi enim ad minim veniam, quis nostrud exerci tation ullamcorper suscipit lobortis nisl ut aliquip ex ea commodo consequat. Duis autem vel eum iriure dolor in hendrerit in vulputate velit esse molestie consequat, vel illum dolore eu feugiat nulla facilisis at vero eros et accumsan et iusto odio dignissim qui blandit praesent luptatum zzril delenit augue duis dolore te feugait nulla facilisi. Lorem ipsum dolor sit amet, consectetuer adipiscing elit, sed diam nonummy nibh euismod tincidunt ut laoreet dolore magna aliquam erat volutpat. Ut wisi enim ad minim veniam, quis nostrud exerci tation ullamcorper suscipit lobortis nisl ut aliquip ex ea commodo consequat. Duis autem vel eum iriure dolor in hendrerit in vulputate velit esse molestie consequat, vel illum dolore eu feugiat nulla facilisis at vero eros et accumsan et iusto odio.</p>
</section>

<section class="section quality">
  <div class="side-label" style="left:42px;top:0"><span>Quality</span></div>
  <div class="heading-mark" style="top:105px"></div>
  <h2 class="heading" style="top:128px">Cut Quality Method</h2>
  <p class="body-text" style="top:180px">Lorem ipsum dolor sit amet, consectetuer adipiscing elit, sed diam nonummy nibh euismod tincidunt ut laoreet dolore magna aliquam erat volutpat. Ut wisi enim ad minim veniam, quis nostrud exerci tation ullamcorper suscipit lobortis nisl ut aliquip ex ea commodo consequat.</p>
  <p class="body-text" style="top:228px;font-weight:700;color:var(--ink)">Comparison to other profile cutting methods such as plasma/laser</p>
  <div class="cuts">
    <div class="cut"><div class="sample" role="img" aria-label="Close-up of Q1 cut edge texture"></div><h4>Separation Cut</h4></div>
    <div class="cut"><div class="sample" role="img" aria-label="Close-up of Q2 cut edge texture"></div><h4>Through Cut</h4></div>
    <div class="cut"><div class="sample" role="img" aria-label="Close-up of Q3 cut edge texture"></div><h4>Clean Cut</h4><p>Typicaly Closer<br>than +/- 0.010"</p></div>
    <div class="cut"><div class="sample" role="img" aria-label="Close-up of Q4 cut edge texture"></div><h4>Good Edge Finish</h4></div>
    <div class="cut"><div class="sample" role="img" aria-label="Close-up of Q5 cut edge texture"></div><h4>Excellent Edge Finish</h4><p>Typicaly Closer<br>than +/- 0.010"</p></div>
  </div>
</section>

<section class="section materials">
  <div class="side-label" style="left:1100px;top:0"><span>Materials</span></div>
  <div class="heading-mark" style="top:100px"></div>
  <h2 class="heading" style="top:124px">Materials</h2>
  <div class="body-text" style="top:176px">
    <p class="lead">It is possible to cut virtually any profile in any material with waterjet.</p>
    <p>Materials we can cut include, but are not limited to, all metals &amp; alloys, stone &amp; ceramics, composites, conen, wood, glass, acrylics, resins, silicones, plastics, foams, carpet and felts. We can also cut laminated dissimilar materials which can often be very hard to cut using conventional methods. We are always happy to test cut a sample of your material free of charge to demonstrate the quality of cut achievable.</p>
    <p>Employing Hydrex's low pressure vacuum assist we can pierce and cut brittle materials such as acrylics and ceramics. In addition AdaptiveJet technology with automatic taper compensation produces more accurate parts at significantly higher cutting speeds than parts cut with a conventional waterjet.</p>
    <p class="cta">If you are not sure whether waterjet cutting will fulfill your requirements give us a call.</p>
  </div>
  <div class="photo-frame" style="top:156px"><div role="img" aria-label="Photograph of a cutting head over a carbon fibre sheet"></div></div>
</section>

<section class="section gallery">
  <div class="side-label" style="left:42px;top:0"><span>Gallery</span></div>
  <div class="heading-mark" style="top:105px"></div>
  <h2 class="heading" style="top:128px">Work Gallery</h2>
  <svg class="arrow" style="left:80px" viewBox="0 0 30 80"><polyline points="24,4 6,40 24,76" fill="none" stroke="#b9c0c5" stroke-width="2"/></svg>
  <svg class="arrow" style="left:1090px" viewBox="0 0 30 80"><polyline points="6,4 24,40 6,76" fill="none" stroke="#b9c0c5" stroke-width="2"/></svg>
  <div class="grid">
    <div class="tile t1" role="img" aria-label="Photograph of sparks from a cutting nozzle"></div>
    <div class="tile t2" role="img" aria-label="Photograph of a waterjet machine at work">
      <div class="overlay"><h5>Lorem Ipsum</h5><p>Lorem ipsum dolor sit amet, consectetuer adipiscing elit, sed diam nonummy nibh euismod tincidunt ut laoreet dolore magna aliquam erat volutpat. Ut wisi enim ad minim veniam, quis nostrud exerci.</p></div>
    </div>
    <div class="tile t3" role="img" aria-label="Photograph of a cutting head under teal light"></div>
    <div class="tile t4" role="img" aria-label="Photograph of machine parts in blue light"></div>
    <div class="tile t5" role="img" aria-label="Photograph of a cutting head under green light"></div>
    <div class="tile t6" role="img" aria-label="Photograph of a cutting head under magenta light"></div>
  </div>
</section>

<section class="section contact" role="img" aria-label="Background photograph of cut metal discs">
  <div class="side-label on-dark" style="left:42px;top:0"><span>Contact Us</span></div>
  <h2 class="heading">Contact Us</h2>
  <div class="info">
    <div class="row">
      <svg width="14" height="18" viewBox="0 0 14 18"><path d="M7 0a7 7 0 0 0-7 7c0 5 7 11 7 11s7-6 7-11a7 7 0 0 0-7-7zm0 10a3 3 0 1 1 0-6 3 3 0 0 1 0 6z" fill="#fff"/></svg>
      <div><b>Brightford Cutworks</b>Unit 6, Kestrel Court, Marlow Road, Ashdown Trade Park<br>Thornbury, Glos, GL7 4QN</div>
    </div>
    <div class="row">
      <svg width="14" height="16" viewBox="0 0 16 16"><path d="M3 1l3 3-2 2c1 2 3 4 6 6l2-2 3 3-2 2C7 15 1 9 1 3z" fill="#fff"/></svg>
      <div>01632 960418</div>
    </div>
    <div class="row">
      <svg width="14" height="12" viewBox="0 0 14 12"><rect x="0.5" y="0.5" width="13" height="11" fill="none" stroke="#fff"/><polyline points="0.5,0.5 7,6 13.5,0.5" fill="none" stroke="#fff"/></svg>
      <div>info@brightfordcutworks.com</div>
    </div>
  </div>
  <div class="form">
    <div class="field">Name</div>
    <div class="pair"><div class="field">Email</div><div class="field">Mobile</div></div>
    <div class="field msg">Message</div>
    <div class="submit">Submit Now <svg width="10" height="14" viewBox="0 0 10 14"><polyline points="2,1 8,7 2,13" fill="none" stroke="#fff" stroke-width="2"/></svg></div>
  </div>
</section>

<footer class="section footer">
  <nav><a>Home</a><a>Contact Us</a><a>Materials</a><a>Gallery</a></nav>
  <div class="brand"><i></i>BRIGHTFORD CUTWORKS</div>
  <p class="copyright">Copyright © 2018 Brightford Cutworks. &nbsp;|&nbsp; All Rights Reserved.</p>
</footer>

</body>
</html>
```